Gym requires a flyer advertising Timetable of Classes

Hello,

Please see the uploaded document brief.txt for details

FLYER SIZE = A5

Thank you,

Industry/Entity Type

Advertising

```html
<!DOCTYPE html>
<html lang="en">
<head>
<meta charset="utf-8">
<title>Ironside Gym – Now Open</title>
<link href="https://fonts.googleapis.com/css2?family=Anton&family=Roboto+Condensed:wght@700&display=swap" rel="stylesheet">
<style>
  :root {
    --stage: #2b2b2b;
    --ink: #0c0c0c;
    --ink-soft: #1f1f1f;
    --red: #e3161b;
    --red-deep: #a80d10;
    --white: #ffffff;
    --ceiling: #3a3030;
    --warm: #b0623e;
    --machine-red: #c8201e;
    --floor: #241c1c;
    --light: #f2c46a;
  }
  * { margin: 0; padding: 0; box-sizing: border-box; }
  html, body { width: 907px; height: 1200px; overflow: hidden; background: var(--stage); }
  .flyer {
    position: absolute; left: 72px; top: 62px; width: 766px; height: 1076px;
    background: radial-gradient(ellipse at 55% 80%, var(--ink-soft), var(--ink) 70%);
    overflow: hidden;
    font-family: "Roboto Condensed", "Arial Narrow", sans-serif;
    font-weight: 700;
    color: var(--white);
  }
  .hero-photo {
    position: absolute; left: 0; top: 0; width: 766px; height: 680px;
    background:
      radial-gradient(ellipse 220px 160px at 300px 390px, rgba(210,120,80,0.75), transparent 70%),
      radial-gradient(ellipse 260px 200px at 520px 300px, rgba(200,32,30,0.7), transparent 70%),
      radial-gradient(ellipse 160px 120px at 90px 300px, rgba(200,32,30,0.75), transparent 70%),
      radial-gradient(ellipse 200px 60px at 700px 230px, rgba(242,196,106,0.35), transparent 70%),
      linear-gradient(180deg, var(--ceiling) 0%, #4a3a36 30%, var(--warm) 55%, var(--machine-red) 70%, var(--floor) 100%);
  }
  .wave { position: absolute; left: 0; top: 0; width: 766px; height: 1076px; }
  .brand-badge {
    position: absolute; left: 80px; top: 486px; width: 200px; height: 200px;
    border-radius: 50%; background: var(--ink); border: 5px solid var(--white);
    display: flex; align-items: center; justify-content: center;
  }
  .brand-badge span { font-size: 32px; color: var(--white); letter-spacing: 1px; }
  .headline {
    position: absolute; right: 41px; top: 600px; text-align: right;
    font-family: "Anton", Impact, sans-serif; font-weight: 400; line-height: 1;
  }
  .headline .name { display: block; font-size: 66px; color: var(--red); }
  .headline .status { display: block; font-size: 68px; color: var(--white); margin-top: 6px; }
  .offer {
    position: absolute; left: 0; width: 766px; top: 786px; text-align: center;
    font-size: 24px; line-height: 30px;
  }
  .classes-call {
    position: absolute; left: 0; width: 766px; top: 860px; text-align: center;
    font-family: "Anton", Impact, sans-serif; font-weight: 400; font-size: 36px; color: var(--red); line-height: 1.1;
  }
  .classes-note {
    position: absolute; left: 0; width: 766px; top: 902px; text-align: center; font-size: 21px;
  }
  .contacts { position: absolute; left: 0; top: 972px; width: 766px; height: 80px; font-size: 21px; }
  .contact { position: absolute; display: flex; align-items: center; gap: 12px; white-space: nowrap; }
  .contact svg { width: 22px; height: 22px; flex: none; }
  .mark { width: 20px; height: 20px; border-radius: 3px; background: var(--red); flex: none; }
</style>
</head>
<body>
<div class="flyer">
  <div class="hero-photo" role="img" aria-label="Photo of a man training on a red leg press machine inside the gym"></div>

  <svg class="wave" viewBox="0 0 766 1076" aria-hidden="true">
    <path d="M0,570 C220,650 420,480 766,410 L766,480 C480,530 260,650 0,660 Z" fill="var(--red-deep)"/>
    <path d="M0,610 C220,670 430,530 766,480 L766,540 C470,565 260,650 0,675 Z" fill="var(--red)"/>
    <path d="M0,675 C260,650 470,565 766,540 L766,1076 L0,1076 Z" fill="var(--ink)"/>
  </svg>

  <div class="brand-badge"><span>IRONSIDE</span></div>

  <h1 class="headline">
    <span class="name">Ironside Gym</span>
    <span class="status">is now open</span>
  </h1>

  <p class="offer">We offer daily, monthly, 3 month, 6 month and annual<br>memberships with absolutely no 'administration' or 'joining fees'!</p>
  <p class="classes-call">Check out our class timetables</p>
  <p class="classes-note">which are free for members!</p>

  <div class="contacts">
    <div class="contact" style="left:40px;top:0">
      <svg viewBox="0 0 22 22"><rect x="1" y="5" width="20" height="13" fill="none" stroke="#fff" stroke-width="2"/><path d="M1,5 L11,13 L21,5" fill="none" stroke="#fff" stroke-width="2"/></svg>
      info@ironsidegym.ae
    </div>
    <div class="contact" style="left:298px;top:0"><span class="mark"></span>@ironsidegymuae</div>
    <div class="contact" style="left:564px;top:0"><span class="mark"></span>/ironsidegymuae</div>
    <div class="contact" style="left:40px;top:52px"><span class="mark"></span>@ironsidegymuae</div>
    <div class="contact" style="left:298px;top:52px">
      <svg viewBox="0 0 22 22"><circle cx="11" cy="11" r="8.5" fill="none" stroke="#fff" stroke-width="2"/><ellipse cx="11" cy="11" rx="3.5" ry="8.5" fill="none" stroke="#fff" stroke-width="1.6"/><path d="M2.5,11 H19.5" stroke="#fff" stroke-width="1.6"/></svg>
      www.ironsidegym.ae
    </div>
    <div class="contact" style="left:564px;top:52px">
      <svg viewBox="0 0 22 22"><path d="M5,2 L8.5,2 L10,7 L7.5,9 C8.8,12 10.2,13.5 13,14.5 L15,12 L20,13.5 L20,17 C20,18.5 18.5,20 17,20 C9,19 3,13 2,5 C2,3.5 3.5,2 5,2 Z" fill="#fff"/></svg>
      04 – 555 0172
    </div>
  </div>
</div>
</body>
</html>
```